Business Card template designs

We need a lot of Business card designs.
Your designs will get exposure on our newly opened business-card printing website.
We are committed to quality of paper and packages we use, so they will come up very fancy.

Here is your advantage. We will put the profile of the graphic designer on our site so that you can showcase your designs to people around the world and in Japan.

A profile is not mandatory, although we encourage graphic designers to have a profile to get continuous work in the future.
We are looking forward to having many good designs.

The right of the use of design will be owned by us.
The design may be used to the products other than
business cards.

Target Market(s)

designer,photographer,creator,artist

Industry/Entity Type

Printing

Contact Information for Business Card

The back design is important.
Please check the reference file.

Requirements
Must have
• Please include the following, required information on your business card designs.
• Name: Haruka Tanabe
• Title: Designer
• Web: https://www.korimo.co.jp/kr/
• Address: 4-17 Kitaharazono-Cho Nerima-ku, Tokyo
• Email: info@kkorimo.com
• Phone: 03 6184 3970
• Mobile: 070 4213 6087
• * For Japanese sites, we will convert the text portion to Japanese characters.
• * In case of 28mmx70mm only include Name,Enail,Phone and SNS account(https://www.facebook.com/kkorimo.com)
• 1. colorful
• 2. simple
• 3. natural
• 4. modern
• 5. cool
• 6. sporty
• Please make variations of the same image with 3-6
• different colors / patterns for one design so that
• customers can compare and choose.
• If you want to use a same picture, please make make
• copies and paste on each different types of design.
Nice to have
• You may also use, the following non-required information.
• Company Name: Korimo, Inc.
• Fax: 03-6471-2093
• Open space for company logo

```html
<!DOCTYPE html>
<html lang="en">
<head>
<meta charset="utf-8">
<title>Korimo business card</title>
<link href="https://fonts.googleapis.com/css2?family=Mulish:wght@400;700;800&display=swap" rel="stylesheet">
<style>
  :root{
    --backdrop:#2a2a2a;
    --card-blue:#06318a;
    --pattern-blue:#0a3795;
    --paper:#f7f7f8;
    --ink-light:#ffffff;
    --s1:#c8163c; --s2:#c8612b; --s3:#d09a2a; --s4:#e1cf3a; --s5:#7cb342;
    --s6:#23913f; --s7:#1e8fd4; --s8:#1c6fc7; --s9:#163e9c; --s10:#5b2c91; --s11:#c2187c;
  }
  *{margin:0;padding:0;box-sizing:border-box}
  html,body{width:1200px;height:987px;overflow:hidden}
  body{background:var(--backdrop);position:relative;font-family:"Mulish",sans-serif;color:var(--ink-light)}
  .card{position:absolute;left:293px;width:615px}
  .card-front{top:131px;height:351px;background:var(--paper)}
  .front-face{position:absolute;left:0;top:0;width:100%;height:324px;background:var(--card-blue)}
  .colour-stripe{position:absolute;left:0;top:324px;width:100%;height:6px;display:flex}
  .colour-stripe span{flex:1}
  .brand-name{position:absolute;left:56px;top:130px;font-size:58px;font-weight:400;letter-spacing:1px;line-height:1}
  .contact-block{position:absolute;left:367px;top:62px;line-height:1}
  .person-name{font-size:22px;font-weight:700}
  .person-title{font-size:18px;margin-top:8px}
  .company{margin-top:12px;font-size:15.5px}
  .company p{margin-bottom:6px}
  .contacts{margin-top:16px;font-size:15.5px;list-style:none}
  .contacts li{display:flex;align-items:center;gap:7px;height:23.5px}
  .contacts svg{width:15px;height:15px;fill:var(--ink-light)}
  .card-back{top:505px;height:352px;background:var(--pattern-blue)}
  .back-pattern{position:absolute;inset:0;background:linear-gradient(180deg,#0b3899,#08338e)}
  .web-address{position:absolute;left:0;right:0;top:168px;text-align:center;font-size:29px;font-weight:800;letter-spacing:1px}
</style>
</head>
<body>
  <section class="card card-front">
    <div class="front-face">
      <div class="brand-name">Korimo</div>
      <div class="contact-block">
        <div class="person-name">Haruka Tanabe</div>
        <div class="person-title">Designer</div>
        <div class="company">
          <p>Korimo, Inc.</p>
          <p>4-17 Kitaharazono-Cho</p>
          <p>Nerima-ku, Tokyo</p>
        </div>
        <ul class="contacts">
          <li><svg viewBox="0 0 16 16"><path d="M3.5 1.5l2.5 3-1.5 1.8c.9 1.9 2.3 3.3 4.2 4.2L10.5 9l3 2.5-1.4 2.8C7 14 2 9 1.7 3z"/></svg>03 6184 3970</li>
          <li><svg viewBox="0 0 16 16"><path d="M4.5 1h7v14h-7zM6 2.5v9.5h4V2.5z"/></svg>070 4213 6087</li>
          <li><svg viewBox="0 0 16 16"><path d="M4 2h8v4H4zM1 7h14v6H1zm2 7h10v1H3z"/></svg>03-6471-2093</li>
          <li><svg viewBox="0 0 16 16"><path d="M1 3.5h14v9H1zm1 .8 6 4.5 6-4.5z"/></svg>info@kkorimo.com</li>
        </ul>
      </div>
    </div>
    <div class="colour-stripe">
      <span style="background:var(--s1)"></span><span style="background:var(--s2)"></span>
      <span style="background:var(--s3)"></span><span style="background:var(--s4)"></span>
      <span style="background:var(--s5)"></span><span style="background:var(--s6)"></span>
      <span style="background:var(--s7)"></span><span style="background:var(--s8)"></span>
      <span style="background:var(--s9)"></span><span style="background:var(--s10)"></span>
      <span style="background:var(--s11)"></span>
    </div>
  </section>

  <section class="card card-back">
    <div class="back-pattern" role="img" aria-label="Faint repeating brand pattern on blue"></div>
    <div class="web-address"><span style="color:var(--s1)">W</span><span style="color:var(--s2)">W</span><span style="color:var(--s3)">W</span><span style="color:#ffffff">.</span><span style="color:var(--s4)">K</span><span style="color:var(--s5)">O</span><span style="color:var(--s6)">R</span><span style="color:var(--s5)">I</span><span style="color:var(--s7)">M</span><span style="color:var(--s7)">O</span><span style="color:#ffffff">.</span><span style="color:var(--s8)">CO</span><span style="color:#ffffff">.</span><span style="color:var(--s8)">JP</span><span style="color:var(--s10)">/</span><span style="color:var(--s11)">KR</span></div>
  </section>
</body>
</html>
```